QuillMintcurrency.net Mobile App

Quillmintcurrency.net is an online Beurea de change. They buy and sell currency from individuals and large corporations.

The app will compliment the main website of the company and focus on specific features as set out in our brief document. overall the design must be high-quality, easy navigate with a one finger operation and nice clean design.

This content is for the design of 3 screen

Loading screen
Homepage screen
Buy Currency for Branch Collection screen

attached is a full brief, but the loading screen will incorporate the logo and the home screen must allow easy navigation to 6 key button features that will enable you to go to each section of the app.

The winner will get to design the remaining screens of the app which are approx 15/18 further screens, based on the same layout.

If you can code the app as well into iPhone and Android, please make this known as well.
Updates

Hello,

For further inspritation for the Home screen, we quite like the interface on the uploaded image velarno-home.jpg

So you slide left and right with your finger to the button, instead of a list format or something quite 2d. Almost 3d like interface maybe with an option to display all as a list?

See what sort of creativity can be achieved.

thanks

Target Market(s)

Consumers mainly aged between 25-60

Industry/Entity Type

It Company

Requirements
Must have
• good clean visually stunning appearance with apply shiny effect buttons and navigation

```html
<!DOCTYPE html>
<html lang="en">
<head>
<meta charset="utf-8">
<title>QuillMint currency – App Screens</title>
<link href="https://fonts.googleapis.com/css2?family=Dosis:wght@600&family=Roboto:wght@300;400;500;700&display=swap" rel="stylesheet">
<style>
  :root {
    --stage: #e5e4e4;
    --blue-dark: #0f5d8f;
    --blue: #1a78b0;
    --blue-light: #2a8cc4;
    --accent-red: #c8262a;
    --tile-red: #c0262b;
    --tile-red-light: #d9544a;
    --tile-red-dark: #8e1519;
    --white: #ffffff;
    --row-bg: #f7f7f7;
    --row-line: #dedede;
    --row-active: #d9e9f7;
    --code-grey: #777777;
    --price-blue: #3d6fb4;
    --chevron: #8a8a8a;
    --order-blue: #17699c;
  }
  * { box-sizing: border-box; margin: 0; padding: 0; }
  html, body { width: 1200px; height: 800px; overflow: hidden; }
  body { background: var(--stage); position: relative; font-family: "Roboto", Arial, sans-serif; }

  .screen { position: absolute; top: 56px; width: 470px; height: 705px; background: var(--white); overflow: hidden; }
  .screen--home { left: 122px; }
  .screen--rates { left: 640px; }

  .bar {
    position: absolute; left: 0; width: 100%;
    background:
      repeating-linear-gradient(135deg, rgba(255,255,255,0.04) 0 2px, transparent 2px 7px),
      linear-gradient(180deg, var(--blue-light), var(--blue) 55%, var(--blue-dark));
  }
  .bar--top { top: 0; border-bottom: 4px solid var(--accent-red); box-shadow: 0 3px 4px rgba(0,0,0,0.15); }
  .bar--bottom { bottom: 0; height: 104px; border-top: 4px solid var(--accent-red); }
  .screen--home .bar--top { height: 200px; }
  .screen--rates .bar--top { height: 106px; }

  .brand { position: absolute; left: 0; width: 100%; text-align: center; color: var(--white); font-weight: 300; line-height: 1; }
  .screen--home .brand { top: 40px; font-size: 50px; }
  .screen--rates .brand { top: 26px; font-size: 24px; }

  .bar-icon { position: absolute; top: 46px; width: 28px; height: 28px; }
  .bar-icon--refresh { left: 29px; }
  .bar-icon--tools { right: 29px; }

  /* Home carousel */
  .carousel { position: absolute; top: 284px; left: 0; width: 100%; height: 160px; perspective: 600px; }
  .tile {
    position: absolute; top: 0; width: 152px; height: 152px; border-radius: 22px;
    background: linear-gradient(180deg, var(--tile-red-light) 0%, var(--tile-red) 48%, #b11e23 52%, var(--tile-red) 100%);
    box-shadow: 0 16px 14px -8px rgba(0,0,0,0.25);
    display: flex; align-items: center; justify-content: center;
  }
  .tile--center { left: 159px; }
  .tile--left { left: 16px; width: 130px; transform: rotateY(32deg); box-shadow: 14px 12px 0 -2px var(--tile-red-dark), 0 18px 14px -8px rgba(0,0,0,0.25); }
  .tile--right { left: 326px; width: 130px; transform: rotateY(-32deg); box-shadow: -14px 12px 0 -2px var(--tile-red-dark), 0 18px 14px -8px rgba(0,0,0,0.25); }
  .tile svg { width: 70px; height: 70px; }

  .prompt { position: absolute; top: 465px; width: 100%; text-align: center; font-family: "Dosis", "Arial Narrow", sans-serif; font-weight: 600; font-size: 23px; letter-spacing: 0.5px; color: var(--accent-red); }
  .pager { position: absolute; top: 530px; left: 180px; width: 110px; height: 36px; display: flex; justify-content: space-between; }
  .pager svg { width: 30px; height: 36px; }

  /* Rates list */
  .rates { position: absolute; top: 112px; left: 0; width: 100%; list-style: none; }
  .rate {
    height: 67px; position: relative; display: flex; align-items: center;
    background: linear-gradient(180deg, var(--white), var(--row-bg));
    border-bottom: 1px solid var(--row-line);
  }
  .rate--active { background: var(--row-active); }
  .rate__code { position: absolute; left: 17px; font-size: 24px; font-weight: 500; color: var(--code-grey); }
  .rate__name { position: absolute; left: 17px; top: 48px; font-size: 11px; color: #333; }
  .rate--named .rate__code { top: 14px; }
  .rate__flag { position: absolute; left: 83px; width: 52px; height: 31px; border: 1px solid #ccc; }
  .rate__price { position: absolute; left: 175px; font-size: 25px; font-weight: 500; color: var(--price-blue); }
  .rate__chevron { position: absolute; right: 17px; width: 12px; height: 18px; }

  .order { position: absolute; top: 538px; left: 15px; width: 446px; height: 46px; display: flex; justify-content: space-between; }
  .order__field { width: 297px; height: 44px; margin-top: 1px; border: 1px solid #ececec; background: var(--white); box-shadow: inset 0 2px 3px rgba(0,0,0,0.06); }
  .order__button { width: 136px; height: 46px; border: none; border-radius: 3px; background: linear-gradient(180deg, #2580b5, var(--order-blue)); color: var(--white); font-family: "Roboto", Arial, sans-serif; font-weight: 500; font-size: 24px; }
</style>
</head>
<body>

<section class="screen screen--home">
  <header class="bar bar--top">
    <div class="brand">QuillMint<br>currency</div>
  </header>

  <div class="carousel">
    <div class="tile tile--left">
      <svg viewBox="0 0 70 70" fill="none" stroke="#fff" stroke-width="3" stroke-linecap="round"><path d="M8 6v54h56"/><path d="M18 52V34M28 52V24M38 52V18M48 52V28M58 52V40"/></svg>
    </div>
    <div class="tile tile--center">
      <svg viewBox="0 0 70 70" fill="none" stroke="#fff" stroke-width="2.5"><ellipse cx="22" cy="40" rx="13" ry="5"/><path d="M9 40v16c0 3 6 5 13 5s13-2 13-5V40"/><ellipse cx="48" cy="26" rx="13" ry="5"/><path d="M35 26v30c0 3 6 5 13 5s13-2 13-5V26"/><path d="M9 46c0 3 6 5 13 5s13-2 13-5M9 51c0 3 6 5 13 5s13-2 13-5M35 33c0 3 6 5 13 5s13-2 13-5M35 40c0 3 6 5 13 5s13-2 13-5M35 47c0 3 6 5 13 5s13-2 13-5"/></svg>
    </div>
    <div class="tile tile--right">
      <svg viewBox="0 0 70 70" fill="none" stroke="#fff" stroke-width="3"><rect x="14" y="6" width="42" height="58" rx="4"/><rect x="21" y="13" width="28" height="11"/><path d="M22 32h5M32 32h5M43 32h5M22 41h5M32 41h5M43 41h5M22 50h5M32 50h5M43 50h5" stroke-linecap="round"/></svg>
    </div>
  </div>

  <p class="prompt">CHOOSE A CURRENCY</p>
  <nav class="pager">
    <svg viewBox="0 0 30 36" fill="none" stroke="#c8262a" stroke-width="5" stroke-linecap="round" stroke-linejoin="round"><path d="M22 4L8 18l14 14"/></svg>
    <svg viewBox="0 0 30 36" fill="none" stroke="#c8262a" stroke-width="5" stroke-linecap="round" stroke-linejoin="round"><path d="M8 4l14 14L8 32"/></svg>
  </nav>

  <footer class="bar bar--bottom">
    <svg class="bar-icon bar-icon--refresh" viewBox="0 0 28 28" fill="none" stroke="#fff" stroke-width="3.5" stroke-linecap="round"><path d="M22 9a9 9 0 1 0 1 8"/><path d="M23 3v7h-7" stroke-linejoin="round"/></svg>
    <svg class="bar-icon bar-icon--tools" viewBox="0 0 28 28" fill="none" stroke="#fff" stroke-width="3" stroke-linecap="round"><path d="M4 24L18 10M19 4a5 5 0 0 0 5 6l-3 3M6 4l18 20"/><path d="M3 7l4-4 3 3-4 4z" fill="#fff"/></svg>
  </footer>
</section>

<section class="screen screen--rates">
  <header class="bar bar--top">
    <div class="brand">QuillMint currency</div>
  </header>

  <ul class="rates">
    <li class="rate">
      <span class="rate__code">USD</span>
      <svg class="rate__flag" viewBox="0 0 52 31" preserveAspectRatio="none"><rect width="52" height="31" fill="#fff"/><g fill="#c0262b"><rect y="0" width="52" height="2.4"/><rect y="4.8" width="52" height="2.4"/><rect y="9.5" width="52" height="2.4"/><rect y="14.3" width="52" height="2.4"/><rect y="19.1" width="52" height="2.4"/><rect y="23.8" width="52" height="2.4"/><rect y="28.6" width="52" height="2.4"/></g><rect width="22" height="16.7" fill="#2b3f7e"/></svg>
      <span class="rate__price">$ 1.0014</span>
      <svg class="rate__chevron" viewBox="0 0 12 18" fill="none" stroke="#8a8a8a" stroke-width="2.5"><path d="M2 2l7 7-7 7"/></svg>
    </li>
    <li class="rate">
      <span class="rate__code">EUR</span>
      <svg class="rate__flag" viewBox="0 0 52 31"><rect width="52" height="31" fill="#27408b"/><g fill="#f2cf1e"><circle cx="26" cy="7" r="1.2"/><circle cx="30.3" cy="8.2" r="1.2"/><circle cx="33.3" cy="11.5" r="1.2"/><circle cx="34.3" cy="15.5" r="1.2"/><circle cx="33.3" cy="19.5" r="1.2"/><circle cx="30.3" cy="22.8" r="1.2"/><circle cx="26" cy="24" r="1.2"/><circle cx="21.7" cy="22.8" r="1.2"/><circle cx="18.7" cy="19.5" r="1.2"/><circle cx="17.7" cy="15.5" r="1.2"/><circle cx="18.7" cy="11.5" r="1.2"/><circle cx="21.7" cy="8.2" r="1.2"/></g></svg>
      <span class="rate__price">€ 1.0014</span>
      <svg class="rate__chevron" viewBox="0 0 12 18" fill="none" stroke="#8a8a8a" stroke-width="2.5"><path d="M2 2l7 7-7 7"/></svg>
    </li>
    <li class="rate">
      <span class="rate__code">GBP</span>
      <svg class="rate__flag" viewBox="0 0 52 31"><rect width="52" height="31" fill="#1f3a7a"/><path d="M0 0l52 31M52 0L0 31" stroke="#fff" stroke-width="6"/><path d="M0 0l52 31M52 0L0 31" stroke="#c8262a" stroke-width="2"/><path d="M26 0v31M0 15.5h52" stroke="#fff" stroke-width="9"/><path d="M26 0v31M0 15.5h52" stroke="#c8262a" stroke-width="5"/></svg>
      <span class="rate__price">£ 1.0014</span>
      <svg class="rate__chevron" viewBox="0 0 12 18" fill="none" stroke="#8a8a8a" stroke-width="2.5"><path d="M2 2l7 7-7 7"/></svg>
    </li>
    <li class="rate rate--active">
      <span class="rate__code">CAD</span>
      <svg class="rate__flag" viewBox="0 0 52 31"><rect width="52" height="31" fill="#fff"/><rect width="13" height="31" fill="#d52b1e"/><rect x="39" width="13" height="31" fill="#d52b1e"/><path d="M26 6l2 4 3-1-1 6 3-2 1 2 2-1-1 4-5 2 1 3h-4v2h-2v-2h-4l1-3-5-2-1-4 2 1 1-2 3 2-1-6 3 1z" fill="#d52b1e"/></svg>
      <span class="rate__price">$ 1.0014</span>
      <svg class="rate__chevron" viewBox="0 0 12 18" fill="none" stroke="#8a8a8a" stroke-width="2.5"><path d="M2 2l7 7-7 7"/></svg>
    </li>
    <li class="rate rate--named">
      <span class="rate__code">JPY</span>
      <span class="rate__name">Japan Yen</span>
      <svg class="rate__flag" viewBox="0 0 52 31"><rect width="52" height="31" fill="#fff"/><circle cx="26" cy="15.5" r="9" fill="#c8262a"/></svg>
      <span class="rate__price">¥ 1.0014</span>
      <svg class="rate__chevron" viewBox="0 0 12 18" fill="none" stroke="#8a8a8a" stroke-width="2.5"><path d="M2 2l7 7-7 7"/></svg>
    </li>
    <li class="rate">
      <span class="rate__code">AUD</span>
      <svg class="rate__flag" viewBox="0 0 52 31"><rect width="52" height="31" fill="#1f3a7a"/><path d="M0 0l24 15M24 0L0 15" stroke="#fff" stroke-width="3"/><path d="M12 0v15M0 7.5h24" stroke="#fff" stroke-width="5"/><path d="M12 0v15M0 7.5h24" stroke="#c8262a" stroke-width="2.5"/><g fill="#fff"><circle cx="12" cy="24" r="2.6"/><circle cx="39" cy="8" r="1.6"/><circle cx="45" cy="14" r="1.6"/><circle cx="34" cy="16" r="1.6"/><circle cx="39" cy="26" r="1.8"/><circle cx="42" cy="19" r="1"/></g></svg>
      <span class="rate__price">$ 1.0014</span>
      <svg class="rate__chevron" viewBox="0 0 12 18" fill="none" stroke="#8a8a8a" stroke-width="2.5"><path d="M2 2l7 7-7 7"/></svg>
    </li>
  </ul>

  <form class="order">
    <input class="order__field" type="text" aria-label="Amount">
    <button class="order__button" type="button">Order</button>
  </form>

  <footer class="bar bar--bottom">
    <svg class="bar-icon bar-icon--refresh" viewBox="0 0 28 28" fill="none" stroke="#fff" stroke-width="3.5" stroke-linecap="round"><path d="M22 9a9 9 0 1 0 1 8"/><path d="M23 3v7h-7" stroke-linejoin="round"/></svg>
    <svg class="bar-icon bar-icon--tools" viewBox="0 0 28 28" fill="none" stroke="#fff" stroke-width="3" stroke-linecap="round"><path d="M4 24L18 10M19 4a5 5 0 0 0 5 6l-3 3M6 4l18 20"/><path d="M3 7l4-4 3 3-4 4z" fill="#fff"/></svg>
  </footer>
</section>

</body>
</html>
```